Business card for a boutique travel agency VELARIEN

we need a business card design - double sided. We would like to have a very elegant, sophisticated but modern design. we are travel consultants and our business focus is Europe, mainly the city of Paris. We would like to receive designs in white and silver, black color but if you are confident that we should pick up a color to make it different and more beautful...go ahead! We are going to give business cards to our clients and business partners. It is important to be perceived as elegant, modern and trustful. Please check jpg references.

Target Market(s)

Velarien primary clients are individuals, couples and affinity groups of high-net-worth who travel for leisure at least once per year. Seeking the ultimate travel experience, the target clients demand the finest quality activities and accommodations accompanied by a superior level of service.

Industry/Entity Type

Travel Industry

Contact Information for Business Card

Lucinda Farrow
- lucinda@velarien-example.com
- +55 11 98347.2516
- velarien-example.com
- unique travel experiences (we would like to see this signature printed as a detail)

Font styles to use
Sans Serif

Colors

Designer to choose colors to be used in the design.

Requirements
Must have
• the Velarien logo that I have attached
Nice to have
• we would like to have some nice detail, something different that shows that we care about,... we are detail oriented.
Should not have
• decorative fonts

```html
<!DOCTYPE html>
<html lang="en">
<head>
<meta charset="utf-8">
<title>Velarien — Business Card</title>
<link rel="stylesheet" href="https://fonts.googleapis.com/css2?family=Open+Sans:wght@300;400&display=swap">
<style>
  :root {
    --backdrop: #8e8e8f;
    --card-front: #262626;
    --card-back: #e4e4e7;
    --accent: #c4501d;
    --ink: #1c1c1e;
  }
  * { margin: 0; padding: 0; box-sizing: border-box; }
  html, body {
    width: 1200px; height: 781px; overflow: hidden;
    background: var(--backdrop);
    font-family: "Open Sans", sans-serif;
  }
  .canvas { position: relative; width: 1200px; height: 781px; }
  .card { position: absolute; left: 358px; width: 453px; height: 251px; }
  .card--front { top: 103px; background: var(--card-front); }
  .card--back { top: 410px; background: var(--card-back); color: var(--ink); }

  .wordmark {
    position: absolute; left: 0; right: 0; top: 114px;
    text-align: center;
    font-weight: 300; font-size: 18px; letter-spacing: 7px;
    padding-left: 7px;
    color: var(--accent);
  }

  .holder-name {
    position: absolute; right: 248px; top: 113px;
    font-size: 19px; font-weight: 400; white-space: nowrap;
  }
  .brand-dot {
    position: absolute; left: 217px; top: 114px;
  }
  .contact-list {
    position: absolute; left: 257px; top: 103px;
    list-style: none; font-size: 11px; line-height: 15px;
  }
  .contact-list li { display: flex; align-items: center; gap: 6px; white-space: nowrap; }
  .contact-list svg { flex: none; }
  .tagline {
    position: absolute; left: 0; right: 0; top: 213px;
    text-align: center; font-size: 11.5px;
  }
</style>
</head>
<body>
<main class="canvas">
  <section class="card card--front" aria-label="Card front">
    <p class="wordmark">VELARIEN</p>
  </section>

  <section class="card card--back" aria-label="Card back">
    <p class="holder-name">Lucinda Farrow</p>
    <svg class="brand-dot" width="24" height="24" viewBox="0 0 24 24" aria-hidden="true">
      <circle cx="12" cy="12" r="10" fill="none" stroke="var(--ink)" stroke-width="2"/>
    </svg>
    <ul class="contact-list">
      <li>
        <svg width="8" height="8" viewBox="0 0 10 10" aria-hidden="true"><path d="M2 1 L4 1 L4.8 3.2 L3.6 4.2 Q4.6 6 5.8 6.4 L6.8 5.2 L9 6 L9 8 Q9 9 8 9 Q1 8.4 1 2 Q1 1 2 1 Z" fill="var(--ink)"/></svg>
        +55 11 98347.2516
      </li>
      <li>
        <svg width="8" height="8" viewBox="0 0 10 10" aria-hidden="true"><rect x="0.5" y="2" width="9" height="6.5" fill="var(--ink)"/><path d="M0.8 2.4 L5 5.6 L9.2 2.4" stroke="var(--card-back)" stroke-width="0.9" fill="none"/></svg>
        lucinda@velarien-example.com
      </li>
      <li>
        <svg width="8" height="8" viewBox="0 0 10 10" aria-hidden="true"><circle cx="5" cy="5" r="4.3" fill="none" stroke="var(--ink)" stroke-width="1"/><ellipse cx="5" cy="5" rx="1.8" ry="4.3" fill="none" stroke="var(--ink)" stroke-width="0.8"/><line x1="0.7" y1="5" x2="9.3" y2="5" stroke="var(--ink)" stroke-width="0.8"/></svg>
        velarien-example.com
      </li>
    </ul>
    <p class="tagline">unique travel experiences</p>
  </section>
</main>
</body>
</html>
```